Moving Company Needs Business Card Design

We need a business cars for moving company based in San Diego. We are called Harborline Moving Systems. We move locally and long distance. 1st side: Logo, website: www.HarborlineMoving.example, Telephone number: 1-855-314-7086.
2nd side: Licensed and Insured,
We move homes and businesses
Services: Local Moving, Long Distance Moving, Loading / Unloading your truck / container, On-site Moving, Packing Service
telephone number 1-855-314-7086, email: info@harborlinemoving.example

```html
<!DOCTYPE html>
<html lang="en">
<head>
<meta charset="utf-8">
<title>Harborline Moving Systems – Business Card</title>
<link href="https://fonts.googleapis.com/css2?family=Tinos:wght@400;700&display=swap" rel="stylesheet">
<style>
  :root {
    --navy: #25214f;
    --red: #e01b2e;
    --ink: #1e1b3a;
    --paper: #ffffff;
    --backdrop: #e4e4e6;
  }
  * { box-sizing: border-box; margin: 0; padding: 0; }
  html, body { width: 1200px; height: 900px; overflow: hidden; }
  body {
    background: var(--backdrop);
    font-family: "Tinos", "Times New Roman", serif;
    color: var(--ink);
    display: flex;
    align-items: center;
    justify-content: center;
    gap: 40px;
  }
  .card {
    position: relative;
    width: 560px;
    height: 320px;
    box-shadow: 0 6px 18px rgba(0,0,0,0.25);
  }
  .card-frame { position: absolute; inset: 0; width: 100%; height: 100%; }
  .card-body { position: absolute; left: 30px; top: 30px; width: 500px; height: 260px; }

  .front .card-body {
    display: flex; flex-direction: column; align-items: center; justify-content: center;
  }
  .brand-name {
    font-weight: 700;
    color: var(--red);
    text-align: center;
    line-height: 1.05;
  }
  .front .brand-name { font-size: 34px; margin-bottom: 14px; }
  .front .web, .front .phone { font-size: 15px; line-height: 1.35; }

  .back .brand-name { font-size: 22px; margin-top: 16px; }
  .tagline { text-align: center; font-size: 18px; line-height: 1.2; margin-top: 6px; }
  .services { position: absolute; left: 12px; top: 138px; }
  .services h2 { font-weight: 400; font-size: 26px; margin-bottom: 6px; }
  .services ul { list-style: none; padding-left: 18px; font-size: 15px; line-height: 1.45; }
  .contact { position: absolute; right: 12px; bottom: 14px; font-size: 13px; line-height: 1.7; }
  .contact li { list-style: none; display: flex; align-items: center; gap: 6px; }
  .contact svg { width: 12px; height: 12px; fill: var(--ink); }
</style>
</head>
<body>

<!-- Front side -->
<section class="card front">
  <svg class="card-frame" viewBox="0 0 560 320" aria-hidden="true">
    <rect width="560" height="320" fill="var(--navy)"/>
    <polygon points="470,0 560,0 560,100" fill="var(--red)"/>
    <polygon points="0,210 0,320 120,320" fill="var(--red)"/>
    <line x1="462" y1="0" x2="560" y2="108" stroke="#fff" stroke-width="4"/>
    <line x1="0" y1="202" x2="128" y2="320" stroke="#fff" stroke-width="4"/>
    <rect x="30" y="30" width="500" height="260" fill="var(--paper)"/>
  </svg>
  <div class="card-body">
    <p class="brand-name">Harborline Moving Systems</p>
    <p class="web">www.HarborlineMoving.example</p>
    <p class="phone">1-855-314-7086</p>
  </div>
</section>

<!-- Back side -->
<section class="card back">
  <svg class="card-frame" viewBox="0 0 560 320" aria-hidden="true">
    <rect width="560" height="320" fill="var(--navy)"/>
    <polygon points="470,0 560,0 560,100" fill="var(--red)"/>
    <polygon points="0,210 0,320 120,320" fill="var(--red)"/>
    <line x1="462" y1="0" x2="560" y2="108" stroke="#fff" stroke-width="4"/>
    <line x1="0" y1="202" x2="128" y2="320" stroke="#fff" stroke-width="4"/>
    <rect x="30" y="30" width="500" height="260" fill="var(--paper)"/>
  </svg>
  <div class="card-body">
    <p class="brand-name">Harborline Moving Systems</p>
    <p class="tagline">Licensed and Insured<br>We move homes and businesses</p>
    <div class="services">
      <h2>Services</h2>
      <ul>
        <li>Local Moving</li>
        <li>Long Distance Moving</li>
        <li>Loading/Unloading your truck/container</li>
        <li>On-site Moving, Packing Service</li>
      </ul>
    </div>
    <ul class="contact">
      <li>
        <svg viewBox="0 0 24 24" aria-hidden="true"><path d="M6.6 10.8a15 15 0 0 0 6.6 6.6l2.2-2.2a1 1 0 0 1 1-.25 11.4 11.4 0 0 0 3.6.57 1 1 0 0 1 1 1V20a1 1 0 0 1-1 1A17 17 0 0 1 3 4a1 1 0 0 1 1-1h3.5a1 1 0 0 1 1 1 11.4 11.4 0 0 0 .57 3.6 1 1 0 0 1-.25 1z"/></svg>
        1-855-314-7086
      </li>
      <li>
        <svg viewBox="0 0 24 24" aria-hidden="true"><path d="M2 4h20v16H2zm2 2v.5l8 5 8-5V6zm0 2.8V18h16V8.8l-8 5z"/></svg>
        info@harborlinemoving.example
      </li>
    </ul>
  </div>
</section>

</body>
</html>
```